Business Card and Letterhead for Juniper Anvil - (Have Logo)

Update 4: Removed company reg no from business card details as it looked a bit out of place. Updated services list.
UPDATE 3
Sorry, I got the address a little bit wrong, have updated it below. Sorry for any inconvenience caused.
UPDATE 2
Finally I have the details for the business cards and letterhead. Submissions already made do not have to be updated unless shortlisted, if all new submissions could include the details for me, Marcus, that would be very much appreciated and help with the final shortlist selection. I intend to share a shortlist of the three best entries with past and existing customers for their feedback and opinions. Thank you all again for your time.
Here are the details.
Marcus Telby
Web Developer
T: 01632 960 418
E: marcus@juniperanvil.example
www.juniperanvil.example
Professional Photography
Web Solutions & E-Commerce
Audio & HD Video Production
Marketing & Promotions
Identity and Branding
Juniper Anvil Ltd
Suite 20938, 3rd Floor
212-224 Orchard Lane
London, N7 9QX
Company Reg. No: 05829147
The order and the layout of the information are of course down to the design, but the company registration number should be smaller and less prominent. The formatting of the telephone and email address using a T: and an E: I am not sure about and again if it is Tel: or Email: or Icons is up to the design.
The Company No. on the letterhead should read (somewhere in small text along the bottom):
Juniper Anvil is a Ltd Company registered in England & Wales, Registration No. 05829147.
The second business card details are
Oliver Brackley
Photographer
T: 01632 960 418
E: oliver@juniperanvil.example
Everything else the same of course.
Thank you again for all the submissions so far.
END OF UPDATE 2
-
UPDATE 1: Please do not alter the logo nor the logo colours. (This was a previous pixel forum project and I am extremely happy with it. The icon can stand alone of course, but I have had to eliminate all entries that have made it black and white, or reversed the icon.) I would like to thank everyone that has participated so far and am very grateful for all your thought and time.
End of Update 1
-
Original Brief:
I have attached the logo vector file.
Following a superb logo from a previous Pixel Forum project I am now looking for a business card design and (although less important) a letterhead as well.
I must admit I tried to do it myself but could only come up with the usual amateur stuff that in comparison to the quality of the logo looked awful.
About Us
Juniper Anvil Ltd will be a new company due to start in January. It is really just me (a web developer) and my friend (a photographer). We will be aiming at the usual small to medium sized businesses in the local area, selling various digital services including photographic services to the public, web hosting and development, commercial photography, modelling services (not us!), full video and film production and possibly a bit of marketing as well. (Really it is anything we can do professionally all lumped together! We met running seperate businesses which have both since closed)
We will not be competing on price. We plan to be expensive but fair. Certainly not the cheapest.
What we are looking for
Business Card
I imagine a double sided business card, which will be used for more than one person. I imagine the front to be the same for everyone and the persons details to be on the back, although this is of course only my thoughts and I am of course completely open to any ideas.
The card could also have a services list or a bit about what we do on it. It might feature the website address, our business address (mail forwarding address) or our registered company number.
Or it might have none of that, we are completely open to any ideas and have no real fixed opinions. I just want it to be really nice :-)
Letterhead (secondary importance)
We will make our decision primarily on the business card, although a mathcing letterhead would be fantastic. Something standardish in format and simple, although again, all ideas are welcomed.
I hope that is enough information but if you have any questions I will answer them as fully and as quickly as possible.
Thank you once again and I really look forward to seeing your ideas and picking a winner.
Marcus T.
Small businesses AND the general public
Film Production

```html
<!DOCTYPE html>
<html lang="en">
<head>
<meta charset="utf-8">
<title>Juniper Anvil – Business Card Concepts</title>
<link href="https://fonts.googleapis.com/css2?family=Arimo:wght@400;700&display=swap" rel="stylesheet">
<style>
  :root {
    --red: #dd0000;
    --charcoal: #333333;
    --white: #ffffff;
    --ink: #111111;
    --rule: #cfcfcf;
    --frame: #555555;
  }
  * { margin: 0; padding: 0; box-sizing: border-box; }
  html, body { width: 1200px; height: 900px; overflow: hidden; background: var(--white); }
  body { position: relative; font-family: "Arimo", Arial, sans-serif; color: var(--ink); }

  .side-label {
    position: absolute; width: 200px; margin-left: -100px; text-align: center;
    font-weight: 700; font-size: 19px; color: var(--ink);
  }

  .card { position: absolute; width: 454px; height: 285px; overflow: hidden; }
  .card--front-light { background: var(--white); border: 1.5px solid var(--frame); }
  .card--front-red { background: var(--red); }
  .card--back-dark { background: var(--charcoal); }
  .card--back-red { background: var(--red); }

  .front-brand {
    position: absolute; left: 0; right: 0; top: 108px;
    display: flex; align-items: center; justify-content: center; gap: 12px;
  }
  .brand-square { width: 28px; height: 28px; background: var(--red); }
  .card--front-red .brand-square { background: var(--white); }
  .brand-name {
    font-weight: 700; font-size: 40px; letter-spacing: 1px; text-transform: uppercase; line-height: 1;
  }
  .card--front-light .brand-name { color: var(--ink); }
  .card--front-red .brand-name { color: var(--white); }

  .corner-mark { position: absolute; right: 30px; bottom: 15px; width: 14px; height: 14px; }

  .holder-name {
    position: absolute; right: 38px; top: 16px;
    font-weight: 700; font-size: 22px; color: var(--white); line-height: 1;
  }
  .brand-band {
    position: absolute; left: 0; right: 0; top: 54px; height: 80px; background: var(--white);
    display: flex; align-items: center; justify-content: flex-end; gap: 7px; padding-right: 38px;
  }
  .brand-band .brand-square { width: 14px; height: 14px; background: var(--red); }
  .brand-band .brand-name { font-size: 21px; color: var(--ink); letter-spacing: 0.5px; }

  .detail-heading {
    position: absolute; top: 158px; font-weight: 700; font-size: 19px; color: var(--white); line-height: 1;
  }
  .detail-heading--address { left: 35px; }
  .detail-heading--contact { right: 38px; }

  .detail-lines { position: absolute; top: 196px; width: 156px; }
  .detail-lines--address { left: 35px; }
  .detail-lines--contact { left: 257px; }
  .detail-lines span { display: block; height: 1.5px; background: var(--rule); margin-bottom: 10px; }
</style>
</head>
<body>
  <div class="side-label" style="left:247px; top:105px;">Front</div>
  <div class="side-label" style="left:838px; top:105px;">Back</div>

  <section class="card card--front-light" style="left:115px; top:143px;">
    <div class="front-brand"><span class="brand-square"></span><span class="brand-name">Juniper Anvil</span></div>
    <svg class="corner-mark" viewBox="0 0 14 14" aria-hidden="true"><polygon points="14,0 14,14 0,14" fill="var(--red)"/></svg>
  </section>

  <section class="card card--back-dark" style="left:602px; top:143px;">
    <div class="holder-name">Marcus Telby</div>
    <div class="brand-band"><span class="brand-square"></span><span class="brand-name">Juniper Anvil</span></div>
    <div class="detail-heading detail-heading--address">Address</div>
    <div class="detail-heading detail-heading--contact">Web / Phone</div>
    <div class="detail-lines detail-lines--address"><span></span><span></span><span></span><span></span><span></span><span></span></div>
    <div class="detail-lines detail-lines--contact"><span></span><span></span><span></span><span></span><span></span><span></span></div>
  </section>

  <div class="side-label" style="left:247px; top:518px;">Front</div>
  <div class="side-label" style="left:840px; top:518px;">Back</div>

  <section class="card card--front-red" style="left:117px; top:555px;">
    <div class="front-brand"><span class="brand-square"></span><span class="brand-name">Juniper Anvil</span></div>
    <svg class="corner-mark" viewBox="0 0 14 14" aria-hidden="true"><polygon points="14,0 14,14 0,14" fill="var(--white)"/></svg>
  </section>

  <section class="card card--back-red" style="left:604px; top:555px;">
    <div class="holder-name">Marcus Telby</div>
    <div class="brand-band"><span class="brand-square"></span><span class="brand-name">Juniper Anvil</span></div>
    <div class="detail-heading detail-heading--address">Address</div>
    <div class="detail-heading detail-heading--contact">Web / Phone</div>
    <div class="detail-lines detail-lines--address"><span></span><span></span><span></span><span></span><span></span><span></span></div>
    <div class="detail-lines detail-lines--contact"><span></span><span></span><span></span><span></span><span></span><span></span></div>
  </section>
</body>
</html>
```